Flyer for Compassion training days

I need a A5-size, single-sided flyer design for my training days. They are weekends in a blend of Orbisan Communication and Buddhist teachings called Verbane Communication. The logo for Verbane that should be included.
The flyer needs room for 1) course title, 2) course dates, location & price, 3) course description, 4) booking info, 5) my picture & short bio, and 6) the verbane.co website (yes, it is 'co' and not 'com).

Target Market(s)

Women 35-65 years, well-educated, spiritually minded. May have interests like yoga and meditation.

Industry/Entity Type

Health And Wellness

Font styles to use
Sans Serif
Other font styles liked:
• Blue Plaque, Josefina are both great

Colors
fbf289
fdf9cf
cfeae6
33b8a4

Requirements
Must have
• The Verbane logo; my picture.
• Elegance. Calm and expansive feel.
• The poster provided in the project files shows you the kind of information I need to include.
• Colours -- greens and yellows, but the options on sketch harbor are not quite the right shades.
• The logo colour can be changed.
Nice to have
• Classy (but not cliche) image associated with Buddhism; gentle curves similar to those on the business card (see project files).
Should not have
• Dark background. Busy, loud design. Overly 'swirly' design. Images that I have to buy separately.

```html
<!DOCTYPE html>
<html lang="en">
<head>
<meta charset="utf-8">
<title>Verbane Communication – Core Course Flyer</title>
<link href="https://fonts.googleapis.com/css2?family=Josefin+Sans:wght@300;400;600;700&display=swap" rel="stylesheet">
<style>
:root{
  --teal:#2fb5a0;
  --teal-deep:#1e8f7e;
  --ink:#2e2e2e;
  --ink-soft:#3c3c3c;
  --brown:#3a2f2c;
  --paper:#f7f7f6;
  --stage:#e9ebe8;
}
*{margin:0;padding:0;box-sizing:border-box}
html,body{width:1200px;height:1199px;overflow:hidden;background:var(--stage)}
body{font-family:"Josefin Sans",sans-serif;color:var(--ink);position:relative}
.flyer{position:absolute;left:213px;top:52px;width:773px;height:1095px;overflow:hidden;
  background:radial-gradient(ellipse at 50% 60%,#ffffff 0%,#f1f1ef 55%,#ebebea 100%);
  box-shadow:0 4px 18px rgba(0,0,0,.12)}
.flyer > *{position:absolute}
.hero-photo{left:0;top:0;width:773px;height:235px;
  background:linear-gradient(180deg,#f4f4f4 0%,#bcbcbc 45%,#6e6e6e 75%,#9a9a9a 100%)}
.hero-hand{right:0;top:60px;width:200px;height:240px;
  background:linear-gradient(200deg,#e2a47c 0%,#f0c6a4 60%,rgba(240,198,164,0) 100%);
  border-radius:60% 0 0 40%}
.hero-wave{left:0;top:140px}
.tagline{left:68px;top:218px;color:var(--teal-deep);font-size:29px;font-weight:400;line-height:33px}
.tagline span{display:block}
.tagline span:first-child{padding-left:35px}
.title{left:62px;top:282px;font-size:67px;font-weight:300;color:var(--ink);letter-spacing:-.5px;white-space:nowrap}
.course-band{left:0;top:358px;width:275px;height:52px;background:var(--teal);
  border-radius:0 0 14px 0;color:#fff;font-size:36px;font-weight:400;padding:8px 0 0 60px}
.details{left:65px;top:415px;font-weight:600;color:var(--ink)}
.details .dates{font-size:28px;line-height:34px}
.details .place{font-size:21px;line-height:27px}
.intro{left:303px;top:367px;width:420px;font-size:20.5px;line-height:27.6px;color:var(--ink-soft)}
.explore{left:68px;top:543px;width:640px;text-align:center;color:var(--teal-deep);font-size:21px;
  padding-bottom:6px;border-bottom:2px solid var(--teal)}
.topics{left:75px;top:588px;width:640px;display:grid;grid-template-columns:378px 1fr;
  list-style:none;row-gap:6px;font-size:18px;font-weight:600;line-height:22px;color:var(--ink-soft)}
.topics li{padding-left:26px;position:relative}
.topics li::before{content:"\2713";position:absolute;left:0;top:0;color:var(--teal);font-weight:400}
.site{left:66px;top:683px;font-size:23px;font-weight:700}
.brand-name{left:78px;top:760px;display:flex;align-items:center;gap:10px;color:var(--teal);
  font-size:30px;font-weight:600}
.brand-name i{display:block;width:18px;height:18px;border-radius:50%;background:var(--teal)}
.audience{left:258px;top:690px;width:460px;font-size:18px;line-height:24px;color:var(--ink-soft);font-weight:400}
.booking-tag{left:254px;top:827px;width:108px;height:30px;background:var(--teal);color:#fff;
  font-size:19px;font-weight:600;text-align:center;padding-top:6px;border-radius:8px 0 8px 0}
.booking-text{left:377px;top:826px;font-size:20.5px;font-weight:600;line-height:27px;color:var(--ink)}
.booking-text a{display:block;padding-left:54px;color:var(--teal-deep);text-decoration:none}
.facilitator-tag{left:254px;top:877px;width:116px;height:30px;background:var(--brown);color:#fff;
  font-size:19px;font-weight:400;padding:6px 0 0 20px;border-radius:8px 0 0 0}
.facilitator-rule{left:254px;top:906px;width:519px;height:2px;background:var(--brown)}
.portrait{left:55px;top:908px;width:186px;height:186px;border-radius:50%;border:3px solid var(--brown);
  background:radial-gradient(circle at 50% 40%,#cfc7bd 0%,#8a7c70 60%,#4a3e36 100%)}
.bio{left:260px;top:922px;width:470px;font-size:18px;line-height:24px;color:var(--ink-soft)}
.bio strong{display:block;margin-top:16px;font-weight:600;color:var(--ink)}
</style>
</head>
<body>
<main class="flyer">
  <div class="hero-photo" role="img" aria-label="Photograph of smooth black stepping stones on still water"></div>
  <svg class="hero-wave" width="773" height="100" viewBox="0 0 773 100" aria-hidden="true">
    <path d="M0 100 L0 70 C180 40 380 65 560 55 C660 50 730 35 773 25 L773 100 Z" fill="#ffffff"/>
    <path d="M0 78 C180 40 380 58 560 45 C660 38 730 22 773 10 L773 28 C730 40 660 58 560 63 C380 72 180 60 0 92 Z" fill="var(--teal)"/>
  </svg>
  <div class="hero-hand" role="img" aria-label="Photograph of an open hand releasing a butterfly"></div>

  <h2 class="tagline"><span>Mindfulness + Kindness +</span><span>Orbisan Communication =</span></h2>
  <h1 class="title">Verbane Communication</h1>

  <div class="course-band">Core Course</div>
  <div class="details">
    <p class="dates">11-12 December</p>
    <p class="place">Larchfield Centre,<br>Edinburgh<br>£125/100</p>
  </div>
  <p class="intro">Verbane Communication can help you increase awareness &amp; compassion in everyday speech (with yourself &amp; others), better understand your own patterns, and build resilience to challenging situations. Choose from:</p>

  <h3 class="explore">In this 2-day Core Course, we’ll explore:</h3>
  <ul class="topics">
    <li>Orbisan Communication;</li>
    <li>mindfulness practices;</li>
    <li>Buddhist teachings on Right Speech, loving-kindness, Right Effort, and more;</li>
    <li>choices available to us in our everyday speech.</li>
  </ul>

  <p class="site">www.verbane.co</p>
  <div class="brand-name"><i></i>Verbane</div>
  <p class="audience">This workshop will be of interest if you’d like to improve personal and/or professional relationships. Open to all, best suited to those with at least 1 year’s experience with Mindfulness, Buddhism, or Orbisan Communication / NVC.</p>

  <div class="booking-tag">booking</div>
  <p class="booking-text">Book online at Ticketlane or write<a href="mailto:morwenna@verbane.co">morwenna@verbane.co</a></p>

  <div class="facilitator-tag">facilitator</div>
  <div class="facilitator-rule"></div>
  <div class="portrait" role="img" aria-label="Portrait photograph of the facilitator"></div>
  <p class="bio">Morwenna Halloway is an experienced group facilitator, having worked with a range of organisations and presented at a number of festivals &amp; conferences.<strong>Morwenna offers coaching in Verbane Communication.</strong></p>
</main>
</body>
</html>
```